Halvercott Orthodontics business card

Using our existing logo (created with ArtFolio), please create a tasteful, contemporary business card. We are father and daughter orthodontists specializing in braces, clarafit, etc to design healthy, beautiful smiles for children, adolescents, and adults. We would like the design to be family-friendly but not childish.
The final design should include all of the information without looking cluttered (I hope! If necessary to achieve an optimal design, please consider making the card double-sided)
Purple, black, silver on a white card
Please include the following information:
Halvercott Orthodontics (logo)
Marguerite L. Halvercott, DMD
Douglas R. Halvercott, DMD

312 Bramblewood Street
North Andover, MA 01899
978.555.0142

847C Quarry Hollow Street
Methuen, MA 01898
978.555.0187

email frontdesk@halvercottortho.example
website www.halvercottortho.example

```html
<!DOCTYPE html>
<html lang="en">
<head>
<meta charset="utf-8">
<title>Halvercott Orthodontics business card</title>
<link rel="stylesheet" href="https://fonts.googleapis.com/css2?family=Lato:wght@300;400;700&family=Montserrat:wght@500;600&display=swap">
<style>
  :root {
    --purple: #6a2a94;
    --purple-light: #7e2f96;
    --purple-dark: #3a0f52;
    --ink: #161616;
    --silver: #858585;
    --paper: #ffffff;
  }
  * { box-sizing: border-box; margin: 0; padding: 0; }
  html, body { width: 1200px; height: 882px; overflow: hidden; background: var(--paper); }
  body { position: relative; font-family: "Lato", sans-serif; }

  .card {
    position: absolute;
    width: 512px;
    height: 306px;
    background: var(--paper);
    box-shadow: 0 1px 5px rgba(0,0,0,0.35);
    overflow: hidden;
  }
  .card--front-douglas { left: 60px; top: 162px; }
  .card--back-a { left: 600px; top: 162px; }
  .card--back-b { left: 60px; top: 499px; }
  .card--front-marguerite { left: 600px; top: 499px; }

  .edge-tab {
    position: absolute;
    top: 127px;
    width: 9px;
    height: 98px;
    background: linear-gradient(90deg, var(--purple-dark), var(--purple-light));
  }
  .edge-tab--right { right: 0; border-radius: 6px 0 0 6px; }
  .edge-tab--left { left: 0; border-radius: 0 6px 6px 0; }

  .brand {
    position: absolute;
    display: flex;
    align-items: center;
    color: var(--purple);
    font-family: "Lato", sans-serif;
    font-weight: 700;
  }
  .brand__dot { border-radius: 50%; background: var(--purple); flex: none; }
  .brand__name { display: flex; flex-direction: column; line-height: 1; }
  .brand__main { letter-spacing: 0.02em; }

  .brand--front { left: 92px; top: 30px; gap: 16px; }
  .brand--front .brand__dot { width: 62px; height: 62px; }
  .brand--front .brand__main { font-size: 40px; }
  .brand--front .brand__sub { font-size: 16px; letter-spacing: 0.42em; margin-top: 6px; }

  .brand--back { left: 0; right: 0; top: 128px; justify-content: center; gap: 12px; }
  .brand--back .brand__dot { width: 46px; height: 46px; }
  .brand--back .brand__main { font-size: 30px; }
  .brand--back .brand__sub { font-size: 12px; letter-spacing: 0.42em; margin-top: 5px; }

  .doctor {
    position: absolute;
    right: 252px;
    top: 140px;
    text-align: right;
  }
  .doctor__name {
    font-family: "Montserrat", sans-serif;
    font-weight: 600;
    font-size: 31px;
    letter-spacing: 0.07em;
    color: var(--ink);
    line-height: 1;
    white-space: nowrap;
  }
  .doctor__name--long {
    font-size: 25px;
    letter-spacing: 0.06em;
    padding-top: 6px;
  }
  .doctor__title {
    font-family: "Montserrat", sans-serif;
    font-weight: 500;
    font-size: 16px;
    letter-spacing: 0.2em;
    color: var(--purple);
    margin-top: 5px;
    margin-right: -0.2em;
    white-space: nowrap;
  }
  .doctor__email {
    font-weight: 400;
    font-size: 14px;
    color: var(--silver);
    margin-top: 2px;
    white-space: nowrap;
  }

  .divider {
    position: absolute;
    left: 284px;
    top: 124px;
    width: 2px;
    height: 99px;
    background: var(--purple);
  }

  .offices {
    position: absolute;
    left: 311px;
    top: 123px;
    font-size: 14px;
    line-height: 17px;
    color: var(--ink);
  }
  .office + .office { margin-top: 3px; }
  .office__phone { color: var(--purple); }

  .swoosh { position: absolute; left: 0; top: 0; width: 512px; height: 306px; }

  .web-band {
    position: absolute;
    left: 0;
    right: 0;
    bottom: 0;
    height: 37px;
    background: linear-gradient(90deg, var(--purple-light), var(--purple-dark));
    color: var(--paper);
    font-size: 17px;
    letter-spacing: 0.12em;
    display: flex;
    align-items: center;
    justify-content: center;
  }
</style>
</head>
<body>

  <section class="card card--front-douglas" aria-label="Business card front, Douglas R. Halvercott">
    <svg class="swoosh" viewBox="0 0 576 344" preserveAspectRatio="none" aria-hidden="true">
      <defs>
        <linearGradient id="swoosh-purple-1" x1="0" y1="0" x2="1" y2="0">
          <stop offset="0" stop-color="#7e2f96"/>
          <stop offset="0.6" stop-color="#4e1468"/>
          <stop offset="1" stop-color="#3a0f52"/>
        </linearGradient>
      </defs>
      <path d="M0 256 C60 300 150 315 270 309 C370 303 420 282 470 282 C520 283 545 318 556 344 L0 344 Z" fill="url(#swoosh-purple-1)"/>
      <path d="M18 243 C80 300 180 310 300 300 C380 292 430 268 480 270 C530 272 562 318 576 344 L556 344 C545 318 522 285 470 285 C420 285 370 306 270 311 C150 317 70 295 18 243 Z" fill="#858585"/>
    </svg>
    <span class="edge-tab edge-tab--right" aria-hidden="true"></span>
    <div class="brand brand--front">
      <span class="brand__dot" aria-hidden="true"></span>
      <span class="brand__name"><span class="brand__main">HALVERCOTT</span><span class="brand__sub">ORTHODONTICS</span></span>
    </div>
    <div class="doctor">
      <p class="doctor__name">DOUGLAS R</p>
      <p class="doctor__title">HALVERCOTT, DMD</p>
      <p class="doctor__email">frontdesk@halvercottortho.example</p>
    </div>
    <span class="divider" aria-hidden="true"></span>
    <div class="offices">
      <p class="office">312 Bramblewood Street<br>North Andover, MA 01899<br><span class="office__phone">978.555.0142</span></p>
      <p class="office">847C Quarry Hollow Street<br>Methuen, MA 01898<br><span class="office__phone">978.555.0187</span></p>
    </div>
  </section>

  <section class="card card--back-a" aria-label="Business card back">
    <span class="edge-tab edge-tab--left" aria-hidden="true"></span>
    <div class="brand brand--back">
      <span class="brand__dot" aria-hidden="true"></span>
      <span class="brand__name"><span class="brand__main">HALVERCOTT</span><span class="brand__sub">ORTHODONTICS</span></span>
    </div>
    <p class="web-band">www.halvercottortho.example</p>
  </section>

  <section class="card card--back-b" aria-label="Business card back">
    <span class="edge-tab edge-tab--left" aria-hidden="true"></span>
    <div class="brand brand--back">
      <span class="brand__dot" aria-hidden="true"></span>
      <span class="brand__name"><span class="brand__main">HALVERCOTT</span><span class="brand__sub">ORTHODONTICS</span></span>
    </div>
    <p class="web-band">www.halvercottortho.example</p>
  </section>

  <section class="card card--front-marguerite" aria-label="Business card front, Marguerite L. Halvercott">
    <svg class="swoosh" viewBox="0 0 576 344" preserveAspectRatio="none" aria-hidden="true">
      <defs>
        <linearGradient id="swoosh-purple-2" x1="0" y1="0" x2="1" y2="0">
          <stop offset="0" stop-color="#7e2f96"/>
          <stop offset="0.6" stop-color="#4e1468"/>
          <stop offset="1" stop-color="#3a0f52"/>
        </linearGradient>
      </defs>
      <path d="M0 256 C60 300 150 315 270 309 C370 303 420 282 470 282 C520 283 545 318 556 344 L0 344 Z" fill="url(#swoosh-purple-2)"/>
      <path d="M18 243 C80 300 180 310 300 300 C380 292 430 268 480 270 C530 272 562 318 576 344 L556 344 C545 318 522 285 470 285 C420 285 370 306 270 311 C150 317 70 295 18 243 Z" fill="#858585"/>
    </svg>
    <span class="edge-tab edge-tab--right" aria-hidden="true"></span>
    <div class="brand brand--front">
      <span class="brand__dot" aria-hidden="true"></span>
      <span class="brand__name"><span class="brand__main">HALVERCOTT</span><span class="brand__sub">ORTHODONTICS</span></span>
    </div>
    <div class="doctor">
      <p class="doctor__name doctor__name--long">MARGUERITE L</p>
      <p class="doctor__title">HALVERCOTT, DMD</p>
      <p class="doctor__email">frontdesk@halvercottortho.example</p>
    </div>
    <span class="divider" aria-hidden="true"></span>
    <div class="offices">
      <p class="office">312 Bramblewood Street<br>North Andover, MA 01899<br><span class="office__phone">978.555.0142</span></p>
      <p class="office">847C Quarry Hollow Street<br>Methuen, MA 01898<br><span class="office__phone">978.555.0187</span></p>
    </div>
  </section>

</body>
</html>
```